Etiketten-Design für Himbeer-Gin
Zielgruppe
GIN
Aufgabenstellung
Wir benötigen ein Etikett für unseren neuen Himbeere GIN, der Name des GINs lautet: KorvalaGIN und soll für folgende Flasche dargestellt werden: https://www.flakoria-beispiel.de/luma-flasche-500ml-schwarz-beschichtet-tqx41-karton-48stk.html
mit dem Etikett https://klebmarken-beispiel.de/anwendungen/fluoreszierende-etiketten/ Himbeerlastiges Design mit bestehendem Logo (WendelGIN) siehe Daten. Bei Fragen stehe ich gerne zur Verfügung!

```html
<!DOCTYPE html>
<html lang="de">
<head>
<meta charset="utf-8">
<title>Korvala Gin – Etikett</title>
<link href="https://fonts.googleapis.com/css2?family=Marcellus&family=Fira+Sans:wght@400;700&display=swap" rel="stylesheet">
<style>
  :root {
    --backdrop: #5a5a5a;
    --label-black: #1a1b1d;
    --raspberry: #e4007f;
    --gold: #b8901a;
    --berry-dark: #2a1622;
  }
  html, body {
    margin: 0;
    padding: 0;
    width: 1200px;
    height: 1062px;
    overflow: hidden;
    background: var(--backdrop);
  }
  .canvas {
    position: relative;
    width: 1200px;
    height: 1062px;
  }
  .label {
    position: absolute;
    left: 370px;
    top: 61px;
    width: 460px;
    height: 940px;
    background: var(--label-black);
    border-radius: 14px;
    box-sizing: border-box;
    padding-top: 64px;
    text-align: center;
  }
  .brand-name {
    margin: 0;
    font-family: "Marcellus", serif;
    font-size: 78px;
    line-height: 1;
    color: var(--raspberry);
    letter-spacing: 1px;
  }
  .brand-gin {
    margin: 4px 0 0;
    font-family: "Marcellus", serif;
    font-size: 118px;
    line-height: 1;
    color: var(--gold);
  }
  .illustration {
    display: block;
    margin: 14px auto 0;
    width: 400px;
    height: 440px;
  }
  .origin {
    margin: 42px 0 0;
    font-family: "Fira Sans", sans-serif;
    font-size: 30px;
    letter-spacing: 1px;
    color: var(--gold);
  }
  .style {
    margin: 4px 0 0;
    font-family: "Fira Sans", sans-serif;
    font-weight: 700;
    font-size: 24px;
    letter-spacing: 1px;
    color: var(--gold);
  }
  .facts {
    position: absolute;
    left: 58px;
    right: 58px;
    bottom: 56px;
    display: flex;
    justify-content: space-between;
    align-items: flex-start;
    font-family: "Fira Sans", sans-serif;
    font-size: 28px;
    line-height: 1.1;
  }
  .volume { color: var(--gold); }
  .abv { color: var(--raspberry); text-align: right; }
</style>
</head>
<body>
  <main class="canvas">
    <section class="label">
      <h1 class="brand-name">Korvala</h1>
      <p class="brand-gin">GIN</p>
      <svg class="illustration" viewBox="0 0 400 440" role="img" aria-label="Illustration: zwei Himbeeren mit goldenen Kelchblättern und Blättern in Pink-Konturen">
        <defs>
          <radialGradient id="berry-tone" cx="50%" cy="55%" r="60%">
            <stop offset="0%" stop-color="#4a1f3a"/>
            <stop offset="100%" stop-color="var(--berry-dark)"/>
          </radialGradient>
        </defs>
        <rect width="400" height="440" rx="16" fill="url(#berry-tone)"/>
      </svg>
      <p class="origin">SCHWÄBISCHER</p>
      <p class="style">DRY GIN</p>
      <div class="facts">
        <span class="volume">0,5l</span>
        <span class="abv">43%<br>Vol</span>
      </div>
    </section>
  </main>
</body>
</html>
```